Flyer Template

I need a flyer template for door knocking on properties. Text Boxes need to be editable, with a header and text body. Footer to be my info. Project to be stylized to match my real estate signs and logo art from past projects

```html
<!DOCTYPE html>
<html lang="en">
<head>
<meta charset="utf-8">
<title>Marlow Realty – Door Knocking Flyer</title>
<link href="https://fonts.googleapis.com/css2?family=Montserrat:wght@700;800&family=Barlow+Semi+Condensed:wght@600&family=Rubik:wght@300;500&display=swap" rel="stylesheet">
<style>
  :root{
    --red:#e21d25;
    --ink:#1f1f1f;
    --text:#2b2b2b;
    --paper:#ffffff;
    --header-grey:#f1f1f2;
    --blue-top:#7c8cc2;
    --blue-bottom:#b6b8dc;
    --footer-black:#1c1a1b;
    --rule:#c9c9c9;
  }
  *{margin:0;padding:0;box-sizing:border-box}
  html,body{width:879px;height:1200px;overflow:hidden;background:var(--paper)}
  .flyer{position:relative;width:879px;height:1200px;background:var(--paper);overflow:hidden;font-family:'Rubik',sans-serif;color:var(--text)}

  .hero-photo{position:absolute;left:0;top:150px;width:879px;height:501px;
    background:linear-gradient(180deg,#a9a6d0 0%,#c9b2c8 28%,#8d8aa6 45%,#6f6f86 62%,#5a5d66 78%,#4f6a46 100%)}
  .header-band{position:absolute;left:0;top:0;width:879px;height:200px}
  .brand-name{position:absolute;left:52px;top:193px;font-family:'Montserrat',sans-serif;font-weight:800;font-size:27px;color:var(--ink);letter-spacing:.3px;display:flex;align-items:center;gap:12px}
  .brand-name{top:auto;bottom:1000px}
  .brand-mark{width:22px;height:22px;background:var(--red)}

  .headline{position:absolute;right:29px;top:98px;text-align:right;font-family:'Montserrat',sans-serif;font-weight:700;font-size:34px;line-height:36px;color:#fff;letter-spacing:.5px}
  .headline-sub{position:absolute;right:37px;top:206px;text-align:right;font-weight:500;font-size:13px;line-height:18px;color:#fff}
  .headline{top:98px}

  .gallery{position:absolute;left:0;top:507px;width:879px;height:250px}
  .gallery-item{position:absolute;top:0;width:236px;height:236px;border-radius:50%;background:#fff;display:flex;align-items:center;justify-content:center;box-shadow:0 16px 14px -12px rgba(0,0,0,.18)}
  .gallery-item .photo{width:214px;height:214px;border-radius:50%}
  .gallery-item:nth-child(1){left:56px}
  .gallery-item:nth-child(2){left:327px}
  .gallery-item:nth-child(3){left:598px}
  .photo-1{background:linear-gradient(180deg,#6aa4e6 0%,#a8c9ee 35%,#8c7d6e 60%,#6a8a4a 85%,#7fb04a 100%)}
  .photo-2{background:linear-gradient(180deg,#c9d6e0 0%,#e6ebee 40%,#bfc3c3 62%,#6f8a4c 85%,#7aa340 100%)}
  .photo-3{background:linear-gradient(180deg,#3d9ae8 0%,#7dbcf0 30%,#8c7f72 55%,#7a7a70 70%,#8aa04a 100%)}

  .section-title{display:flex;align-items:flex-start;gap:12px;font-family:'Barlow Semi Condensed',sans-serif;font-weight:600;font-size:31px;line-height:33px;text-transform:uppercase;color:var(--ink)}
  .section-title .accent{color:var(--red)}
  .title-mark{flex:none;width:22px;height:22px;margin-top:6px;border:3px solid var(--red)}

  .about{position:absolute;left:40px;top:771px;width:400px}
  .about .section-title{margin-left:0}
  .about-body{margin:18px 0 0 1px;font-weight:300;font-size:15.5px;line-height:20.5px;color:var(--text)}
  .about-body p+p{margin-top:20px}

  .divider{position:absolute;left:469px;top:806px;width:1px;height:282px;background:linear-gradient(180deg,transparent,var(--rule) 15%,var(--rule) 85%,transparent)}

  .services{position:absolute;left:515px;top:773px;width:340px}
  .services .section-title{font-size:33px}
  .service-list{list-style:none;margin-top:18px}
  .service-list li{display:flex;align-items:center;gap:10px;height:25.5px;font-weight:300;font-size:16px;letter-spacing:.2px;color:var(--text)}
  .service-list svg{flex:none;width:13px;height:13px}

  .agent{position:absolute;left:39px;top:1077px}
  .agent-name{font-family:'Montserrat',sans-serif;font-weight:800;font-size:31px;line-height:34px;color:var(--red);letter-spacing:.5px}
  .agent-contact{display:flex;align-items:center;gap:8px;margin-top:3px;font-family:'Montserrat',sans-serif;font-weight:700;font-size:12.5px;color:var(--ink);letter-spacing:.3px}
  .agent-contact svg{width:12px;height:12px}
  .agent-contact .gap{width:8px}

  .office{position:absolute;left:430px;top:1078px;width:449px;height:47px;display:flex}
  .office-brand{width:176px;background:var(--footer-black);display:flex;align-items:center;justify-content:center;font-family:'Barlow Semi Condensed',sans-serif;font-weight:600;font-size:17px;color:#fff;letter-spacing:.3px}
  .office-note{flex:1;background:var(--red);display:flex;align-items:center;justify-content:center;text-align:center;font-family:'Montserrat',sans-serif;font-weight:700;font-size:10.5px;line-height:13px;color:#fff;font-variant:small-caps;letter-spacing:.6px}
</style>
</head>
<body>
<main class="flyer">
  <div class="hero-photo" role="img" aria-label="Two-storey grey suburban house with a double garage and lit windows at dusk under a pink and violet sky"></div>

  <svg class="header-band" viewBox="0 0 879 200" preserveAspectRatio="none" aria-hidden="true">
    <defs>
      <linearGradient id="headerBlue" x1="0" y1="0" x2="0" y2="1">
        <stop offset="0" stop-color="#7c8cc2"/>
        <stop offset="1" stop-color="#a8acd6"/>
      </linearGradient>
    </defs>
    <rect x="0" y="0" width="879" height="200" fill="url(#headerBlue)"/>
    <polygon points="0,0 497,0 413,200 0,200" fill="#f1f1f2"/>
    <polygon points="60,0 200,0 330,200 190,200" fill="#ffffff" opacity=".55"/>
  </svg>

  <div class="brand-name"><span class="brand-mark"></span>MARLOW REALTY</div>

  <h1 class="headline">LOREM IPSUM<br>IS SIMPLY<br>DUMMY TEXT</h1>
  <p class="headline-sub">Lorem Ipsum is simply dummy text of the printing<br>and typesetting industry.</p>

  <div class="gallery">
    <div class="gallery-item"><div class="photo photo-1" role="img" aria-label="Family home with stone porch and dormer windows on a green lawn"></div></div>
    <div class="gallery-item"><div class="photo photo-2" role="img" aria-label="Modern white terraced houses with glass balconies"></div></div>
    <div class="gallery-item"><div class="photo photo-3" role="img" aria-label="Large stone-faced house with a curved driveway and lawn"></div></div>
  </div>

  <section class="about">
    <h2 class="section-title"><span class="title-mark"></span><span><span class="accent">Lorem Ipsum is</span><br>Simply dummy text</span></h2>
    <div class="about-body">
      <p>Lorem Ipsum is simply dummy text of the printing and typesetting industry. Lorem Ipsum has been the industry's standard dummy text ever since the 1500s,</p>
      <p>Lorem Ipsum is simply dummy text of the printing and typesetting industry. Lorem Ipsum has been the industry's standard dummy text ever since the 1500s,</p>
    </div>
  </section>

  <div class="divider"></div>

  <section class="services">
    <h2 class="section-title"><span class="title-mark"></span><span><span class="accent">Our</span> Services</span></h2>
    <ul class="service-list">
      <li><svg viewBox="0 0 14 14"><circle cx="7" cy="7" r="6" fill="none" stroke="#e21d25" stroke-width="1.6"/><path d="M4.2 7.2l2 2 3.6-3.8" fill="none" stroke="#e21d25" stroke-width="1.6"/></svg>Lorem Ipsum is simply dummy</li>
      <li><svg viewBox="0 0 14 14"><circle cx="7" cy="7" r="6" fill="none" stroke="#e21d25" stroke-width="1.6"/><path d="M4.2 7.2l2 2 3.6-3.8" fill="none" stroke="#e21d25" stroke-width="1.6"/></svg>Text of the printing and</li>
      <li><svg viewBox="0 0 14 14"><circle cx="7" cy="7" r="6" fill="none" stroke="#e21d25" stroke-width="1.6"/><path d="M4.2 7.2l2 2 3.6-3.8" fill="none" stroke="#e21d25" stroke-width="1.6"/></svg>Typesetting industry.</li>
      <li><svg viewBox="0 0 14 14"><circle cx="7" cy="7" r="6" fill="none" stroke="#e21d25" stroke-width="1.6"/><path d="M4.2 7.2l2 2 3.6-3.8" fill="none" stroke="#e21d25" stroke-width="1.6"/></svg>Lorem Ipsum has been the</li>
      <li><svg viewBox="0 0 14 14"><circle cx="7" cy="7" r="6" fill="none" stroke="#e21d25" stroke-width="1.6"/><path d="M4.2 7.2l2 2 3.6-3.8" fill="none" stroke="#e21d25" stroke-width="1.6"/></svg>Industry's standard dummy</li>
      <li><svg viewBox="0 0 14 14"><circle cx="7" cy="7" r="6" fill="none" stroke="#e21d25" stroke-width="1.6"/><path d="M4.2 7.2l2 2 3.6-3.8" fill="none" stroke="#e21d25" stroke-width="1.6"/></svg>Text ever since the 1500s,</li>
      <li><svg viewBox="0 0 14 14"><circle cx="7" cy="7" r="6" fill="none" stroke="#e21d25" stroke-width="1.6"/><path d="M4.2 7.2l2 2 3.6-3.8" fill="none" stroke="#e21d25" stroke-width="1.6"/></svg>Lorem Ipsum is simply dummy</li>
      <li><svg viewBox="0 0 14 14"><circle cx="7" cy="7" r="6" fill="none" stroke="#e21d25" stroke-width="1.6"/><path d="M4.2 7.2l2 2 3.6-3.8" fill="none" stroke="#e21d25" stroke-width="1.6"/></svg>Text of the printing and</li>
    </ul>
  </section>

  <footer>
    <div class="agent">
      <div class="agent-name">JORDAN MARLOW</div>
      <div class="agent-contact">
        <svg viewBox="0 0 24 24"><path d="M6.6 10.8a15.1 15.1 0 0 0 6.6 6.6l2.2-2.2c.3-.3.7-.4 1-.2 1.1.4 2.3.6 3.6.6.6 0 1 .4 1 1V20c0 .6-.4 1-1 1A17 17 0 0 1 3 4c0-.6.4-1 1-1h3.5c.6 0 1 .4 1 1 0 1.3.2 2.5.6 3.6.1.3 0 .7-.2 1z" fill="#e21d25"/></svg>
        <span>555-014-2290</span>
        <span class="gap"></span>
        <svg viewBox="0 0 24 24"><rect x="2" y="5" width="20" height="14" fill="#e21d25"/><path d="M2 5l10 8 10-8" fill="none" stroke="#fff" stroke-width="1.8"/></svg>
        <span>JMARLOW@MAILBOX.EXAMPLE</span>
      </div>
    </div>
    <div class="office">
      <div class="office-brand">NORTHBAY GROUP</div>
      <div class="office-note">Each office independently<br>owned and operated</div>
    </div>
  </footer>
</main>
</body>
</html>
```